Online-Marketing Material für Chatterloop Werbeanzeigen
Zielgruppe
Wir sind ein Brötchen Bringdienst. Unsere Zielgruppe sind junge Familien mit Kindern.
Aufgabenstellung
Ich benötige das Design für Chatterloop werbeanzeigen.
Wir werben gerne mit unserer kostenlosen Probesendung.
Bitte beachten: Wir heißen NOCH Tafelglück. Ändern aber in kurzer Zeit den Namen in die MORGENKORBHAUS. Deshalb bitte schon den neuen Namen verwenden.

```html
<!DOCTYPE html>
<html lang="de">
<head>
<meta charset="utf-8">
<title>MORGENKORBHAUS – Deine Brötchen ofenfrisch geliefert</title>
<link rel="stylesheet" href="https://fonts.googleapis.com/css2?family=Michroma&family=Poppins:wght@700;800&family=Montserrat:wght@500&display=swap">
<style>
  :root {
    --bg-dark: #3b3b3d;
    --orange: #f28b1d;
    --orange-deep: #d9620e;
    --white: #ffffff;
    --kitchen-light: #ece8e2;
    --skin-beige: #c9ab8e;
    --shirt-blue: #4f8fc6;
    --table-warm: #b88a62;
    --bread-light: #f8c26c;
    --bread-dark: #d97a22;
  }
  * { margin: 0; padding: 0; box-sizing: border-box; }
  html, body { width: 1200px; height: 630px; overflow: hidden; background: var(--bg-dark); }
  .ad {
    position: relative;
    width: 1200px;
    height: 630px;
    overflow: hidden;
    background:
      radial-gradient(ellipse 420px 260px at 1000px 200px, rgba(140,140,142,.45), transparent 70%),
      radial-gradient(ellipse 380px 220px at 850px 420px, rgba(120,120,122,.35), transparent 70%),
      var(--bg-dark);
  }
  .family-photo {
    position: absolute;
    left: 0; top: 0;
    width: 760px; height: 560px;
    background: linear-gradient(165deg,
      var(--kitchen-light) 0%,
      #e2d6c8 22%,
      var(--skin-beige) 40%,
      #7ea6cc 55%,
      var(--shirt-blue) 66%,
      var(--table-warm) 85%,
      #d9c7b2 100%);
    clip-path: polygon(0 0, 700px 0, 690px 60px, 712px 150px, 695px 250px, 725px 330px, 705px 420px, 740px 480px, 640px 520px, 420px 540px, 160px 530px, 0 520px);
  }
  .bread-rolls {
    position: absolute;
    left: 0; top: 0;
    width: 760px; height: 630px;
  }
  .badge {
    position: absolute;
    left: 520px; top: 25px;
    width: 206px; height: 206px;
    border-radius: 50%;
    background: var(--orange);
    display: flex; align-items: center; justify-content: center;
  }
  .badge-text {
    font-family: "Poppins", sans-serif;
    font-weight: 800;
    color: var(--white);
    font-size: 27px;
    line-height: 1.28;
    text-align: center;
    letter-spacing: 1px;
    transform: rotate(-9deg);
  }
  .brand {
    position: absolute;
    left: 760px; top: 139px;
    width: 410px;
    text-align: center;
    font-family: "Montserrat", sans-serif;
    font-weight: 500;
    font-size: 20px;
    letter-spacing: 6px;
    color: var(--orange);
  }
  .headline {
    position: absolute;
    left: 745px; top: 216px;
    width: 440px;
    text-align: center;
    font-family: "Michroma", sans-serif;
    font-weight: 400;
    color: var(--white);
    line-height: 1.1;
  }
  .headline-small { display: block; font-size: 31px; margin-bottom: 12px; }
  .headline-large { display: block; font-size: 44px; margin-bottom: 10px; }
  .cta {
    position: absolute;
    left: 770px; top: 438px;
    width: 370px; height: 107px;
    border-radius: 54px;
    background: var(--orange-deep);
    display: flex; align-items: center; justify-content: center;
    text-align: center;
    font-family: "Poppins", sans-serif;
    font-weight: 700;
    font-size: 21px;
    line-height: 1.55;
    letter-spacing: 2px;
    color: var(--white);
  }
  .pointer-icon {
    position: absolute;
    left: 1062px; top: 505px;
    width: 92px; height: 92px;
  }
</style>
</head>
<body>
  <main class="ad">
    <div class="family-photo" role="img" aria-label="Foto: junge Familie mit Kindern am Frühstückstisch, die Mutter reicht einen Teller mit Brötchen"></div>

    <svg class="bread-rolls" viewBox="0 0 760 630" role="img" aria-label="Illustration: Gruppe goldbrauner Brötchen und Kaisersemmeln im Vordergrund">
      <defs>
        <linearGradient id="bread-tone" x1="0" y1="410" x2="0" y2="630" gradientUnits="userSpaceOnUse">
          <stop offset="0" stop-color="var(--bread-light)"/>
          <stop offset="1" stop-color="var(--bread-dark)"/>
        </linearGradient>
      </defs>
      <g fill="url(#bread-tone)">
        <circle cx="180" cy="545" r="48"/>
        <circle cx="262" cy="560" r="60"/>
        <circle cx="355" cy="522" r="62"/>
        <circle cx="487" cy="550" r="82"/>
        <circle cx="560" cy="490" r="52"/>
        <circle cx="632" cy="460" r="52"/>
        <circle cx="655" cy="560" r="72"/>
      </g>
    </svg>

    <div class="badge">
      <p class="badge-text">EINFACH<br>FRISCH<br>SCHNELL</p>
    </div>

    <p class="brand">MORGENKORBHAUS</p>

    <h1 class="headline">
      <span class="headline-small">DEINE BRÖTCHEN</span>
      <span class="headline-large">OFENFRISCH</span>
      <span class="headline-large">GELIEFERT</span>
    </h1>

    <a class="cta">JETZT GRATIS<br>PROBIEREN</a>

    <svg class="pointer-icon" viewBox="0 0 82 82" aria-hidden="true">
      <path d="M10 6 L44 40 L44 30 C44 26 52 26 52 30 L52 40 C52 36 60 36 60 40 L60 46 C60 42 68 42 68 46 L68 62 C68 72 60 78 50 78 L40 78 C33 78 28 74 24 68 L14 52 C12 48 17 44 21 48 L28 56 L4 12 C2 8 7 3 10 6 Z"
            fill="#ffffff" stroke="#2b2b2b" stroke-width="3" stroke-linejoin="round"/>
    </svg>
  </main>
</body>
</html>
```